Ridge 4 Ridge Turbine Rentals Pty Ltd

We are a hire company based on the Gold Coast in Australia, we Hire out Generators to construction sites, music festivals, parties, fetes etc. Anywhere where power is required we can provide it.

Ridge 4 Ridge Turbine Rentals pty Ltd also provides all leads, distribution boards, Qualified Electricians to perform all connections. we offer refuelling services and mechanical services. 24Hr on call service - to an actual english speaking operator.

Slogan ''Steady Current Every Site"

Industry/Entity Type

Construction

Contact Information for Business Card

M: 0481265390
E: bookings@ridge4ridgeturbinerentals-example.com.au

```html
<!DOCTYPE html>
<html lang="en">
<head>
<meta charset="utf-8">
<title>Ridge 4 Ridge Turbine Rentals – Business Card</title>
<link rel="stylesheet" href="https://fonts.googleapis.com/css2?family=Source+Sans+3:wght@400;600;700&display=swap">
<style>
  :root {
    --bg: #e9e7e4;
    --card: #ffffff;
    --ink: #1c1c1c;
    --brand: #2d6990;
    --band-dark: #33698f;
    --band-light: #a9d5e4;
    --band-pale: #d9eef5;
    --icon: #2d6990;
  }
  * { margin: 0; padding: 0; box-sizing: border-box; }
  html, body { width: 1200px; height: 1000px; overflow: hidden; }
  body {
    background: var(--bg);
    font-family: "Source Sans 3", "Myriad Pro", Arial, sans-serif;
    color: var(--ink);
    position: relative;
  }
  .card {
    position: absolute;
    left: 265px;
    width: 665px;
    height: 397px;
    background: var(--card);
    border-radius: 24px;
    overflow: hidden;
    box-shadow: 0 4px 14px rgba(0,0,0,0.18);
  }
  .card--front { top: 73px; }
  .card--back { top: 533px; }

  .brand {
    position: absolute;
    display: flex;
    align-items: center;
    gap: 16px;
    color: var(--brand);
    font-weight: 700;
    text-transform: uppercase;
    line-height: 1.05;
  }
  .brand__mark {
    flex: none;
    background: var(--brand);
  }
  .brand__name span { display: block; }

  .card--front .brand {
    left: 0; right: 0; top: 178px;
    justify-content: center;
    font-size: 34px;
  }
  .card--front .brand__mark { width: 70px; height: 70px; }

  .tagline {
    position: absolute;
    left: 0; right: 0; top: 336px;
    text-align: center;
    font-size: 17px;
  }

  .card--back .brand {
    left: 40px; top: 62px;
    font-size: 27px;
  }
  .card--back .brand__mark { width: 56px; height: 56px; }

  .contact {
    position: absolute;
    right: 38px;
    top: 196px;
    text-align: right;
  }
  .contact__name { font-size: 21px; font-weight: 600; }
  .contact__role { font-size: 16px; margin-top: 2px; }
  .contact__lines { margin-top: 26px; font-size: 15.5px; }
  .contact__line {
    display: flex;
    justify-content: flex-end;
    align-items: center;
    gap: 8px;
    height: 23px;
  }
  .contact__line svg { width: 16px; height: 14px; fill: var(--icon); }

  .band {
    position: absolute;
    left: 0; right: 0; bottom: 0;
    height: 50px;
    display: flex;
  }
  .band__dark { width: 330px; background: var(--band-dark); }
  .band__light { flex: 1; background: linear-gradient(90deg, var(--band-pale) 0%, var(--band-light) 35%, var(--band-light) 100%); }
</style>
</head>
<body>

<section class="card card--front">
  <div class="brand">
    <div class="brand__mark"></div>
    <div class="brand__name"><span>Ridge 4 Ridge</span><span>Turbine Rentals</span></div>
  </div>
  <p class="tagline">Steady Current Every Site</p>
</section>

<section class="card card--back">
  <div class="brand">
    <div class="brand__mark"></div>
    <div class="brand__name"><span>Ridge 4 Ridge</span><span>Turbine Rentals</span></div>
  </div>

  <div class="contact">
    <p class="contact__name">Darren Holt</p>
    <p class="contact__role">Director of Operrations</p>
    <div class="contact__lines">
      <p class="contact__line">0481265390
        <svg viewBox="0 0 16 14" aria-hidden="true"><path d="M1 5 C1 2 4 1 8 1 C12 1 15 2 15 5 L11.5 5.5 L11 3.5 C9 3 7 3 5 3.5 L4.5 5.5 Z"/><path d="M3 7 L5 5.5 L11 5.5 L13 7 L13 13 L3 13 Z"/></svg>
      </p>
      <p class="contact__line">bookings@ridge4ridgeturbinerentals-example.com.au
        <svg viewBox="0 0 16 14" aria-hidden="true"><path d="M1 2 H15 V12 H1 Z M2 3 L8 8 L14 3" fill="var(--icon)" stroke="#fff" stroke-width="1"/></svg>
      </p>
    </div>
  </div>

  <div class="band">
    <div class="band__dark"></div>
    <div class="band__light"></div>
  </div>
</section>

</body>
</html>
```